Tovimerra: Travel business card redesign

We need a clean elegant look for our cards featuring blue and orange. Look should communicate a sense of strong design and seem uncluttered. The company is Tovimerra which means escape to bliss. As in every trip is an escape to bliss. Feel free to reinvent the logo or just tweak it. Colors should be blue like Caribbean waters and a saturated orange. Keep it clean and simple.
Please match the information in the sample uploaded but the sample is horrible -- a non-starter -- use for information only. also please add managing director to my name as title

Target Market(s)
potential clients, hotels, trade publications
Industry/Entity Type
Travel Industry
Contact Information for Business Card
as above
Requirements
Must have
- Font should be century gothic. Colors below are close but a but prefer lighter in each case.

```html
<!DOCTYPE html>
<html lang="en">
<head>
<meta charset="utf-8">
<title>Tovimerra Business Card</title>
<link rel="stylesheet" href="https://fonts.googleapis.com/css2?family=Didact+Gothic&display=swap">
<style>
  :root {
    --stage: #4d4d4d;
    --ink-dark: #061920;
    --navy: #0c2535;
    --orange: #ff7f00;
    --orange-deep: #cc5200;
    --logo-orange: #ee6a2c;
    --sky: #6ab0e0;
    --white: #ffffff;
  }
  html, body {
    margin: 0;
    width: 1200px;
    height: 1200px;
    overflow: hidden;
    background: var(--stage);
  }
  .card {
    position: absolute;
    left: 110px;
    width: 980.8px;
    height: 544.8px;
    display: block;
    font-family: "Didact Gothic", "Century Gothic", sans-serif;
  }
  .card--front { top: 28px; }
  .card--back { top: 627.2px; }
  .fill-dark { fill: var(--ink-dark); }
  .fill-navy { fill: var(--navy); }
  .fill-orange { fill: var(--orange); }
  .fill-orange-deep { fill: var(--orange-deep); }
  .brand-name { fill: var(--logo-orange); font-size: 84px; }
  .site-url { fill: var(--white); font-size: 49px; }
  .site-tagline { fill: var(--white); font-size: 19px; }
  .site-dot { fill: var(--white); }
  .person-name { fill: var(--sky); font-size: 84px; }
  .person-title { fill: var(--sky); font-size: 36px; }
  .contact-line { fill: var(--sky); font-size: 41px; }
</style>
</head>
<body>

<svg class="card card--front" viewBox="0 0 1226 681" aria-label="Tovimerra business card, front">
  <defs>
    <linearGradient id="front-sheen" x1="0" y1="0" x2="0" y2="1">
      <stop offset="0" stop-color="#e2e2e2"/>
      <stop offset="0.75" stop-color="#ffffff"/>
    </linearGradient>
  </defs>
  <rect class="front-background" width="1226" height="681" fill="url(#front-sheen)"/>
  <polygon class="fill-dark" points="0,0 743,0 528,340 0,340"/>
  <polygon class="fill-orange-deep" points="743,0 810,0 595,362 528,340"/>
  <polygon class="fill-navy" points="0,340 360,340 250,455 223,484 555,484 710,681 0,681"/>
  <polygon class="fill-orange" points="360,340 528,340 595,362 250,455"/>
  <polygon class="fill-orange" points="598,540 750,540 850,681 708,681"/>
  <polygon class="fill-orange-deep" points="768,566 885,566 965,681 848,681"/>
  <polygon class="fill-dark" points="905,595 1000,595 1060,681 963,681"/>

  <text class="brand-name" x="748" y="208">Tovimerra</text>

  <circle class="site-dot" cx="68" cy="591" r="3.5"/>
  <circle class="site-dot" cx="80" cy="591" r="3.5"/>
  <circle class="site-dot" cx="97" cy="591" r="7"/>
  <text class="site-url" x="287" y="605" text-anchor="middle">tovimerra.com</text>
  <circle class="site-dot" cx="476" cy="591" r="7"/>
  <circle class="site-dot" cx="493" cy="591" r="3.5"/>
  <circle class="site-dot" cx="505" cy="591" r="3.5"/>
  <text class="site-tagline" x="287" y="635" text-anchor="middle">a first in service company</text>
</svg>

<svg class="card card--back" viewBox="0 0 1226 681" aria-label="Tovimerra business card, back">
  <rect class="back-background" width="1226" height="681" fill="var(--white)"/>
  <polygon class="fill-dark" points="0,0 448,0 255,291 155,238 0,238"/>
  <polygon class="fill-orange-deep" points="448,0 518,0 325,328 255,291"/>
  <polygon class="fill-orange" points="155,238 325,328 95,386"/>
  <polygon class="fill-navy" points="0,238 155,238 95,386 0,616"/>

  <polygon class="fill-orange-deep" points="1226,102 1226,275 1077,522 993,496"/>
  <polygon class="fill-dark" points="1077,522 1226,275 1226,681 1131,541"/>
  <polygon class="fill-navy" points="1131,541 1226,681 1143,681"/>
  <polygon class="fill-orange" points="993,496 1077,522 1131,541 1143,681"/>

  <text class="person-name" x="861" y="156" text-anchor="middle">Arlen Voss</text>
  <text class="person-title" x="861" y="198" text-anchor="middle">Managing Director</text>

  <text class="contact-line" x="135" y="438">o: 866.55.TOVIM (86846)</text>
  <text class="contact-line" x="135" y="488">m: 555.214.3380</text>
  <text class="contact-line" x="135" y="538">f: 555.480.2917</text>
  <text class="contact-line" x="135" y="589">1460 Harlow Crest Way N.</text>
  <text class="contact-line" x="135" y="639">Seaview Bay, 90817</text>
</svg>

</body>
</html>
```